Hi,

I would like to have a invitation made for a party. exactly like the picture in the link below.

http://pinboardia.example/pin/730215948361027459/

However, Please change the colors into fun/ girly feeling. font can be different and size of the card should be the same

Name of the girl: RINA
What: Bachelorette Party
Where:TOLO Boat
Dubai Coral Quay Sailing Club
When:7th of February 2013

No RSVP required. (so no need to put it)

```html
<!DOCTYPE html>
<html lang="en">
<head>
<meta charset="utf-8">
<title>Rina's Bachelorette Party Invitation</title>
<link rel="stylesheet" href="https://fonts.googleapis.com/css2?family=Rye&family=Smokum&family=Ewert&family=Oswald:wght@300;400&display=swap">
<style>
  :root {
    --paper: #fffad6;
    --rose: #cf6f6a;
    --cocoa: #85705e;
    --scarlet: #e8373a;
    --stone: #a9a08f;
    --flourish: #c9c2ac;
  }
  html, body {
    margin: 0;
    padding: 0;
    overflow: hidden;
    background: var(--paper);
  }
  .invitation {
    position: relative;
    width: 1200px;
    height: 550px;
    background: var(--paper);
    overflow: hidden;
  }
  .flourish {
    position: absolute;
    background: var(--flourish);
  }
  .flourish--corner {
    width: 64px;
    height: 64px;
    border-radius: 50% 18% 50% 18%;
  }
  .flourish--top-left { left: 12px; top: 14px; }
  .flourish--top-right { left: 327px; top: 14px; }
  .flourish--bottom-left { left: 12px; top: 474px; }
  .flourish--bottom-right { left: 327px; top: 474px; }
  .flourish--divider {
    height: 30px;
    border-radius: 50%;
  }
  .flourish--headline { left: 480px; top: 103px; width: 158px; }
  .flourish--details { left: 882px; top: 481px; width: 240px; }

  .headline {
    position: absolute;
    left: 0;
    top: 0;
    width: 800px;
    height: 550px;
  }
  .headline__name {
    font-family: "Rye", serif;
    fill: var(--rose);
    font-size: 104px;
  }
  .headline__tagline {
    font-family: "Smokum", serif;
    fill: var(--cocoa);
    font-size: 74px;
  }
  .headline__single {
    font-family: "Ewert", serif;
    fill: var(--scarlet);
    font-size: 196px;
  }

  .details {
    position: absolute;
    left: 880px;
    top: 104px;
    width: 244px;
    margin: 0;
    text-align: center;
    font-family: "Oswald", sans-serif;
    font-weight: 300;
    color: var(--stone);
    text-transform: uppercase;
    font-size: 18px;
    line-height: 1;
  }
  .details p { margin: 0; }
  .details__event { font-weight: 400; letter-spacing: 0.5px; }
  .details__at { margin-top: 52px !important; }
  .details__venue { margin-top: 17px !important; }
  .details__club { margin-top: 32px !important; }
  .details__on { margin-top: 24px !important; }
  .details__date { margin-top: 25px !important; }
</style>
</head>
<body>
<main class="invitation">
  <div class="flourish flourish--corner flourish--top-left" role="img" aria-label="Ornamental corner flourish"></div>
  <div class="flourish flourish--corner flourish--top-right" role="img" aria-label="Ornamental corner flourish"></div>
  <div class="flourish flourish--corner flourish--bottom-left" role="img" aria-label="Ornamental corner flourish"></div>
  <div class="flourish flourish--corner flourish--bottom-right" role="img" aria-label="Ornamental corner flourish"></div>
  <div class="flourish flourish--divider flourish--headline" role="img" aria-label="Ornamental scroll divider"></div>

  <svg class="headline" viewBox="0 0 800 550" aria-label="Rina's last chance to celebrate being single">
    <text class="headline__name" x="31" y="181" textLength="341" lengthAdjust="spacingAndGlyphs">RINA’S</text>
    <text class="headline__tagline" x="35" y="263" textLength="340" lengthAdjust="spacingAndGlyphs">LAST CHANCE TO</text>
    <text class="headline__tagline" x="412" y="263" textLength="366" lengthAdjust="spacingAndGlyphs">CELEBRATE BEING</text>
    <text class="headline__single" x="31" y="451" textLength="747" lengthAdjust="spacingAndGlyphs">SINGLE</text>
  </svg>

  <section class="details">
    <p class="details__event">Bachelorette Party</p>
    <p class="details__at">At</p>
    <p class="details__venue">TOLO Boat</p>
    <p class="details__club">Dubai Coral Quay Sailing Club</p>
    <p class="details__on">On</p>
    <p class="details__date">7th of February 2013</p>
  </section>

  <div class="flourish flourish--divider flourish--details" role="img" aria-label="Ornamental scroll divider"></div>
</main>
</body>
</html>
```